Medical centre needs a business card

We are a medcial centre in Australia, needing a new business card. Our demographic is low working class families. We are going to be renovating our premises to modernise the look and also had a new logo done a few months ago representing quality and community, and now need to update our cards. It needs to be doubled sided, with logo and contact details on the front, and appointment details on the back. . Needs to be modern and simple, easy to read. <br/><br/>Name: Fern Vale Medical Centre <br/>Address: 512 Kestrel Rd (Cnr Kestrel Rd & Lindon Park Rd),<br/>Corvane Court Shopping Centre, Paralowie, SA 5108<br/>Ph: 08 8361 4027<br/>Tag line: Where every visit counts for you<br/>Website: www.fernvalemedicalcentre.example.au<br/>Online bookings also available<br/><br/>(On the back, to have 3 lines of appointments that can be written in.<br/>Day, date, time)<br/><br/>Your next appointment is on<br/>Can try “M T W Th F Sa Su _________________ at ____________ am/pm” or other combinations <br/>Please advise as soon as possible if unable to attend<br/>Cancellation fees apply if less than 2 hrs notice<br/>Online appointments available (please highlight this option by either by position, colour or font)

Target Market(s)

Lower social economic working class, young families to seniors

Industry/Entity Type

Medical Centre

Contact Information for Business Card

Fern Vale Medical Centre
512 Kestrel Rd (Cnr Kestrel Rd & Lindon Park Drive)
Corvane Court Shopping Centre
Marrowby SA 5192
Ph: 08 8361 4027
www.fernvalemedicalcentre.example.au
Tagline line: where every visit counts for you
Back side is for appointments
Your next appointment is with Dr ______________
Day/date/time (Please give 3 lines of appointments)
Please advise as soon as possible if unable to attend
Cancellation fees apply if less than 2 hours notice
Online appointments available
Book online easily and conveniently (please highlight online appointments)

Font styles to use
Serif
Sans Serif

Colors

Designer to choose colors to be used in the design.

Requirements
Must have
• Modern and simple
• Easy to ready
• Induces a wellbeing feeling
• Incorporate our logo colours and feel from logo
• Induces feeling of stability and security
Nice to have
• Attract attention
• Pleasant to look at
• Feeling of innovation
Should not have
• Loud clashing colours
• Overly luxurious feeling
• Overly artistic

```html
<!DOCTYPE html>
<html lang="en">
<head>
<meta charset="utf-8">
<title>Fern Vale Medical Centre – Business Card</title>
<link rel="stylesheet" href="https://fonts.googleapis.com/css2?family=Roboto:wght@400;500;700;900&display=swap">
<style>
  :root {
    --blue: #1a7cc9;
    --blue-dark: #1565a8;
    --green: #8cc63f;
    --ink: #3a3a3a;
    --grey: #5b5b5b;
    --rule: #9a9a9a;
    --card: #ffffff;
    --backdrop: #e4e4e4;
  }
  * { box-sizing: border-box; margin: 0; padding: 0; }
  html, body { width: 1200px; height: 800px; overflow: hidden; }
  body {
    background: var(--backdrop);
    font-family: "Roboto", Arial, sans-serif;
    display: flex;
    align-items: center;
    justify-content: center;
    gap: 40px;
  }
  .card {
    position: relative;
    width: 560px;
    height: 320px;
    background: var(--card);
    box-shadow: 0 6px 18px rgba(0,0,0,.18);
  }

  /* Front */
  .brand {
    position: absolute;
    left: 34px; top: 118px;
    width: 210px;
    display: flex; align-items: center; gap: 12px;
  }
  .brand__mark {
    flex: none;
    width: 34px; height: 34px;
    border-radius: 50%;
    background: var(--green);
  }
  .brand__name {
    color: var(--blue);
    font-weight: 900;
    font-size: 24px;
    line-height: 1.05;
    text-transform: uppercase;
  }
  .divider {
    position: absolute;
    left: 262px; top: 36px;
    width: 1px; height: 190px;
    background: var(--rule);
  }
  .contact {
    position: absolute;
    left: 280px; top: 34px;
    width: 270px;
    color: var(--grey);
    font-size: 12.5px;
    line-height: 1.45;
  }
  .contact__name {
    color: var(--blue);
    font-weight: 700;
    font-size: 21px;
    text-transform: uppercase;
    line-height: 1.1;
  }
  .contact__role {
    color: var(--green);
    font-weight: 500;
    font-size: 14px;
    margin-bottom: 8px;
  }
  .contact__company { color: var(--ink); font-weight: 700; font-size: 13px; }
  .contact__lines { margin-bottom: 8px; }
  .contact__row { display: flex; align-items: center; gap: 6px; }
  .contact__row svg { width: 11px; height: 11px; fill: var(--blue); flex: none; }
  .tagline {
    position: absolute;
    left: 0; right: 0; bottom: 34px;
    text-align: center;
    color: var(--blue);
    font-weight: 500;
    font-size: 17px;
    letter-spacing: 1.5px;
    text-transform: uppercase;
  }

  /* Back */
  .appt { padding: 30px 34px 0; color: var(--blue); }
  .appt__title {
    text-align: center;
    font-size: 21px;
    font-weight: 500;
    letter-spacing: 1px;
    margin-bottom: 22px;
  }
  .field {
    display: flex; align-items: flex-end; gap: 6px;
    font-size: 13px; font-weight: 500;
    text-transform: uppercase;
    margin-bottom: 20px;
    white-space: nowrap;
  }
  .field__line {
    flex: 1;
    border-bottom: 1px dotted var(--rule);
    height: 12px;
  }
  .field__unit { margin-left: 2px; }
  .blank-line {
    border-bottom: 1px dotted var(--rule);
    height: 12px;
    margin-bottom: 20px;
  }
  .appt__notice {
    text-align: center;
    color: var(--grey);
    font-size: 11.5px;
    line-height: 1.35;
  }
  .appt__online {
    text-align: center;
    color: var(--blue-dark);
    font-weight: 900;
    font-size: 16px;
    text-transform: uppercase;
    margin-top: 8px;
  }
</style>
</head>
<body>

<section class="card card--front">
  <div class="brand">
    <span class="brand__mark"></span>
    <span class="brand__name">Fern Vale Medical Centre</span>
  </div>
  <div class="divider"></div>
  <div class="contact">
    <p class="contact__name">Daniel Hartley</p>
    <p class="contact__role">President</p>
    <div class="contact__lines">
      <p class="contact__company">Fern Vale Medical Centre</p>
      <p>512 Kestrel Rd</p>
      <p>(Cnr Kestrel Rd &amp; Lindon Park Drive)</p>
      <p>Corvane Court Shopping Centre</p>
      <p>Marrowby SA 5192</p>
    </div>
    <p class="contact__row">
      <svg viewBox="0 0 24 24" aria-hidden="true"><path d="M6.6 10.8a15.1 15.1 0 0 0 6.6 6.6l2.2-2.2c.3-.3.7-.4 1-.2 1.1.4 2.3.6 3.6.6.6 0 1 .4 1 1V20c0 .6-.4 1-1 1A17 17 0 0 1 3 4c0-.6.4-1 1-1h3.5c.6 0 1 .4 1 1 0 1.3.2 2.5.6 3.6.1.3 0 .7-.2 1z"/></svg>
      08 8361 4027
    </p>
    <p class="contact__row">
      <svg viewBox="0 0 24 24" aria-hidden="true"><path d="M12 2a10 10 0 1 0 0 20 10 10 0 0 0 0-20zm6.9 6h-2.9a15.7 15.7 0 0 0-1.4-3.6A8 8 0 0 1 18.9 8zM12 4a14 14 0 0 1 1.9 4h-3.8A14 14 0 0 1 12 4zM4.3 14a8 8 0 0 1 0-4h3.4a16.5 16.5 0 0 0 0 4zm.8 2h2.9c.3 1.3.8 2.5 1.4 3.6A8 8 0 0 1 5.1 16zM8 8H5.1a8 8 0 0 1 4.3-3.6C8.8 5.5 8.3 6.7 8 8zm4 12a14 14 0 0 1-1.9-4h3.8A14 14 0 0 1 12 20zm2.3-6H9.7a14.7 14.7 0 0 1 0-4h4.6a14.7 14.7 0 0 1 0 4zm.3 5.6c.6-1.1 1.1-2.3 1.4-3.6h2.9a8 8 0 0 1-4.3 3.6zm1.8-5.6a16.5 16.5 0 0 0 0-4h3.4a8 8 0 0 1 0 4z"/></svg>
      fernvalemedicalcentre.example.au
    </p>
  </div>
  <p class="tagline">Where every visit counts for you</p>
</section>

<section class="card card--back">
  <div class="appt">
    <h2 class="appt__title">APPOINTMENTS</h2>
    <div class="field">Your next appointment is with Dr :<span class="field__line"></span></div>
    <div class="field">Day :<span class="field__line"></span>Date :<span class="field__line"></span>Time :<span class="field__line"></span><span class="field__unit">AM/PM</span></div>
    <div class="field">Note :<span class="field__line"></span></div>
    <div class="blank-line"></div>
    <p class="appt__notice">Please advise as soon as possible if unable to attend Cancellation fees<br>apply if less than 2 hours notice Online appointments available</p>
    <p class="appt__online">Book online easily &amp; conveniently</p>
  </div>
</section>

</body>
</html>
```